Photography Company Seeks Amazing and Fun Website Design

Note: This is for design only. No coding required. We want to see your ideas for a great website! This will be a FUN design and not boring like others you may work on.

Please let your creative ideas flow. We have given you a ton of info along with videos to help you understand what we are after, however we WANT your creativity to shine through in your designs!

We are a professional company that has run hundreds of crowdsourced projects on multiple platforms. If you participate in this contest (we hope you do) you can expect great video feedback, consistent feedback, and also our guarantee that if we know your website design will not be what we are looking for we will notify you so you don’t waste your time if there is no chance of you winning.

We respect and recognize this is how you make your living and we will not play games. We look forward to an awesome contest and awesome website designs.

Design Brief:

We are looking for a stunning website design to showcase this amazing photography company. Their current site is:

http://www.kelvaprints.example/

As you can see they do amazing photography and need an amazing website to showcase their work and to attract new people into their studios.

We are looking to get a website that is clean, classy, bright, artistic, and that really helps this company stand out amongst other photography companies.

We need a homepage and an interior page mockup.

Here are some examples of other sites in their business with what we like:

http://www.tabrowenstudio.example/

Please watch video to learn what we like and don’t like:http://clipvault.example/t/QpR4sz7LmWd

http://www.holbrinkimaging.example/

Please watch video to learn what we like and don’t like: http://clipvault.example/t/Hb8ufN2kxyPa

NOTE: We do not want to copy anything outright. We want to learn, model and take their ideas and make them better. We also want to be flexible and take what we like along with your creativity to make an amazing design.

Here is what we are looking for in more specific terms:

NOTE: Website should have a spot for video on the homepage.

This website is for a very professional and well know photography company. Because it is photography the website needs to be VERY visual.

Site should be unique and really stand out to help sell the business and their services. EVERYTHING about this business is visual, so the site MUST reflect that.

Site Overall: Fun and Artistic. This is a forward thinking company that is fun, upbeat, and does things differently, they need the design to reflect that. This is a modern photography company.

They also do all kinds of photography from school kids, sports teams, in studio shoots with High School Seniors, Family Pictures etc.

Colors: We like the white background because it is clean and really helps the photos stand out. Also please look at the logo too. Use colors from that and make things flow. Again we want this to stand out and be different while at the same time being clean.

Menu: Horizontal. We like bold and easy to read menu items. Don’t make it small and cluttered. Include the same items that are in the other site for the mock up.

Site Structure: Clean and easy to navigate. We have a lot of content to display so we need a clean structure that breaks up the text and content areas.

Images: Please pull images from the current site. We can always replace the images of course, but if you show them “their own stuff” in the new design you will be closer to winning because it will feel more like “them”

Content Areas: It is a safe bet that if it is on the current site we need it on the new site. So don’t drop anything as it makes it hard to “cut content”.

What we don't want: We do not want clutter, boring, or templates or themes. We don’t want too cartoony, too cute, or too fancy. We don’t want ugly.

Out of respect to professional designers who really are working hard to win if you do not follow this brief, you submit worn out themes, templates, or boring designs you will be eliminated. We are offering great prize money for this so we expect great visual designs.

Thanks,

The Solvane Team

Target Market(s)

Target Market are upper middle class who want a better photography studio then the average studio, but don't want to go to the highest end of photography. This studio will cater to higher middle class.

Industry/Entity Type

Business

Number of Pages Required

1 page

Font styles to use
Sans Serif

Requirements
Must have
• Video on Home page
• Clean
• Stand Out
• Fun
• Professional
Nice to have
• Creative
• Lots of content in a great structure
Should not have
• clutter
• ugly design
• messy

```html
<!DOCTYPE html>
<html lang="en">
<head>
<meta charset="utf-8">
<title>Kelva Photography – Home</title>
<link rel="stylesheet" href="https://fonts.googleapis.com/css2?family=Josefin+Sans:wght@300;400;600;700&family=Montserrat:wght@400;600;700&display=swap">
<style>
:root{
  --accent:#e5461c;
  --accent-dark:#c9380f;
  --page:#efefef;
  --white:#ffffff;
  --ink:#3a3a3a;
  --muted:#8a8a8a;
  --heading-gray:#8c8c8c;
  --panel-dark:#2e2e2e;
  --footer-dark:#2a2a2a;
  --video-blue:#27a6e6;
}
*{box-sizing:border-box;margin:0;padding:0}
html,body{width:1200px;height:2222px;overflow:hidden}
body{background:var(--page);font-family:"Josefin Sans",Arial,sans-serif;color:var(--ink);position:relative}
.abs{position:absolute}

/* header */
.site-header{left:93px;top:0;width:1014px;height:81px;background:var(--white)}
.brand{left:8px;top:14px;display:flex;align-items:center;gap:10px}
.brand-name{font-size:40px;font-weight:400;color:var(--ink);line-height:1}
.brand-dot{width:18px;height:18px;border-radius:50%;background:var(--accent)}
.main-nav{left:326px;top:48px;display:flex;gap:21px;font-size:14px;font-weight:600;color:#222;letter-spacing:.4px;white-space:nowrap;line-height:1}
.main-nav span{white-space:nowrap}
.main-nav .active{color:var(--accent);position:relative}
.main-nav .active::after{content:"";position:absolute;left:0;right:0;top:22px;height:3px;background:var(--accent)}
.social-top{left:900px;top:10px;display:flex;gap:8px}
.social-top span{width:20px;height:20px;display:block}

.tagline{left:93px;top:116px;font-family:"Montserrat",Arial,sans-serif;font-weight:700;font-size:31px;letter-spacing:1.5px;color:var(--heading-gray)}
.follow-pill{left:867px;top:94px;width:238px;height:34px;border-radius:17px;background:var(--white);border:1px solid #ddd;font-size:15px;color:#555;display:flex;align-items:center;padding-left:24px;gap:12px;white-space:nowrap}
.follow-pill i{width:20px;height:20px;background:#6b5446;border-radius:4px;display:block}

.book-btn{background:var(--accent);color:var(--white);border-radius:3px;box-shadow:0 2px 0 var(--accent-dark);display:flex;flex-direction:column;justify-content:center;line-height:1.25;white-space:nowrap}
.book-btn b{font-family:"Montserrat",Arial,sans-serif;letter-spacing:1px}
.book-top{left:94px;top:169px;width:223px;height:64px;padding-left:22px;font-size:17px}
.book-top b{font-size:16px}

/* hero slider */
.hero{left:94px;top:263px;width:1013px;height:389px;overflow:hidden}
.hero-photo{position:absolute;inset:0;background:linear-gradient(125deg,#8f86a6 0%,#c6b6d4 30%,#e7ccd0 55%,#8d8aa4 80%,#6f6a80 100%)}
.hero-prev{position:absolute;left:0;top:0;width:30px;height:100%;background:var(--accent);display:flex;align-items:center;justify-content:center}
.hero-next{position:absolute;right:8px;top:178px}
.hero-caption{position:absolute;left:504px;top:176px;width:482px;height:213px;background:rgba(45,40,45,.78);color:var(--white);padding:26px 16px}
.hero-caption h2{font-family:"Montserrat",Arial,sans-serif;font-weight:600;font-size:24px;line-height:1.35;letter-spacing:1px}
.hero-caption p{font-size:19px;line-height:1.4;font-weight:300}
.read-more{position:absolute;left:193px;top:168px;width:122px;height:36px;background:var(--accent);border-radius:2px;font-size:14px;display:flex;align-items:center;justify-content:center}

/* welcome */
.welcome{left:94px;top:706px;width:500px}
.welcome h3{color:var(--accent);font-size:19px;font-weight:700;margin-bottom:14px}
.welcome p{font-size:12px;line-height:1.55;color:#444;margin-bottom:12px}
.service-list{list-style:none;font-size:12px;color:#444}
.service-list li{display:flex;gap:10px;margin-bottom:9px;line-height:1.45}
.service-list li::before{content:"";flex:none;width:12px;height:12px;border-radius:50%;background:var(--accent);margin-top:1px}
.welcome .call-line{color:var(--accent);font-size:15px;margin-top:18px;line-height:1.3}
.call-line small{font-size:13px;display:block}

.tile{width:226px;height:195px;top:709px}
.tile-studio{left:611px;background:linear-gradient(180deg,#8a8c92 0%,#5e5a5a 45%,#3a3434 70%,#7b2024 100%)}
.tile-sports{left:854px;background:linear-gradient(120deg,#c9c3cf 0%,#8b9bb5 40%,#3c4a6a 60%,#5e8a3f 100%)}
.tile-icon{position:absolute;width:18px;height:18px;background:rgba(30,30,30,.8);color:#fff;font-size:14px;display:flex;align-items:center;justify-content:center}
.studio-panel{left:611px;top:904px;width:226px;height:194px;background:var(--panel-dark);border-top:3px solid var(--accent);padding:26px 18px;color:#ccc;z-index:2}
.studio-panel h4{color:var(--accent);font-size:16px;font-weight:400;padding-bottom:10px;border-bottom:1px solid #555;margin-bottom:10px}
.studio-panel p{font-size:12px;line-height:1.55}

/* service cards */
.card{top:1074px;width:202px;height:271px;background:var(--white);box-shadow:0 6px 0 #dcdcdc}
.card-photo{height:143px}
.card h5{font-size:19px;font-weight:400;text-align:center;padding:14px 0 10px;border-bottom:1px solid #e6e6e6;margin:0 10px;white-space:nowrap}
.card p{font-size:11px;line-height:1.55;color:#555;padding:10px 14px}
.carousel-arrow{top:1176px}

/* video */
.video-heading{left:0;width:1200px;top:1404px;text-align:center;font-family:"Montserrat",Arial,sans-serif;font-weight:700;font-size:34px;color:var(--heading-gray);letter-spacing:1px}
.video-sub{left:0;width:1200px;top:1456px;text-align:center;font-size:13px;color:#666;line-height:1.5}
.video{left:202px;top:1522px;width:800px;height:465px;overflow:hidden}
.video-frame{position:absolute;inset:0;background:linear-gradient(90deg,#3a3a3e 0%,#4a5a78 35%,#2f7fc4 62%,#2e6fb3 100%)}
.video-thumb{position:absolute;left:18px;top:16px;width:72px;height:72px;background:linear-gradient(#5a7fb0,#7c5e52);border:2px solid #fff}
.video-title{position:absolute;left:98px;top:16px;background:rgba(20,20,20,.85);padding:8px 12px;font-family:"Montserrat",Arial,sans-serif;font-size:21px;color:var(--video-blue);white-space:nowrap}
.video-from{position:absolute;left:98px;top:64px;background:rgba(20,20,20,.85);padding:4px 12px;font-size:15px;color:#fff}
.video-from span{color:var(--video-blue)}
.video-actions{position:absolute;right:20px;top:18px;display:flex;flex-direction:column;gap:8px}
.video-actions div{width:62px;height:46px;background:rgba(20,20,20,.85);color:#fff;font-size:10px;font-family:"Montserrat",Arial,sans-serif;font-weight:700;display:flex;flex-direction:column;align-items:center;justify-content:flex-end;padding-bottom:5px;gap:4px}
.video-controls{position:absolute;left:16px;right:16px;bottom:18px;height:56px;display:flex;gap:8px}
.play-btn{width:102px;background:rgba(20,20,20,.85);display:flex;align-items:center;justify-content:center}
.scrub{flex:1;background:rgba(20,20,20,.85);position:relative;display:flex;align-items:center;padding:0 16px;gap:14px}
.track{flex:1;height:12px;background:#666;position:relative}
.track .loaded{position:absolute;left:0;top:0;bottom:0;width:58%;background:#999}
.track .played{position:absolute;left:0;top:0;bottom:0;width:43%;background:var(--video-blue)}
.time-tag{position:absolute;left:210px;top:-28px;background:#222;color:#fff;font-size:13px;padding:3px 6px;font-family:"Montserrat",Arial,sans-serif}
.hd{color:var(--video-blue);font-family:"Montserrat",Arial,sans-serif;font-weight:700;font-size:16px;font-style:normal}

/* footer */
.footer-brand{left:94px;top:2026px}
.footer-brand .brand{position:static}
.footer-brand .brand-name{font-size:40px}
.footer-brand .sub{font-size:17px;font-weight:700;color:#222;margin-top:6px}
.book-bottom{left:937px;top:2050px;width:170px;height:50px;padding-left:16px;font-size:14px}
.book-bottom b{font-size:12px}
.footer-bar{left:0;top:2158px;width:1200px;height:64px;background:var(--footer-dark);color:#777;font-size:12px;display:flex;align-items:center;padding-left:96px;gap:40px}
.footer-social{position:absolute;right:94px;top:24px;display:flex;gap:14px}
.footer-social span{width:16px;height:16px;border-radius:3px;background:#6d6d6d;display:block}
.footer-social span.on{background:var(--video-blue)}
</style>
</head>
<body>

<header class="site-header abs">
  <div class="brand abs"><span class="brand-name">Kelva</span><span class="brand-dot"></span></div>
  <nav class="main-nav abs">
    <span class="active">HOME</span><span>STUDIO</span><span>SUPER SENIOR DAYS</span><span>BOOK IT!</span><span>ORDERING</span><span>SPORTS</span><span>CONTACT US</span>
  </nav>
  <div class="social-top abs" aria-label="Social links">
    <span style="background:#3b5a98"></span><span style="background:#3aa4dc"></span><span style="background:#e8694b"></span>
  </div>
</header>

<h1 class="tagline abs">LIVE THIS MOMENT FOREVER</h1>
<div class="follow-pill abs">Follow us on PhotoFeed <i></i></div>
<div class="book-btn book-top abs">Click here to book your<b>KELVA EXPERIENCE</b></div>

<section class="hero abs">
  <div class="hero-photo" role="img" aria-label="Film strips of senior, family and sports portraits against a lilac sky"></div>
  <div class="hero-prev"><svg width="12" height="20" viewBox="0 0 12 20"><path d="M10 2 L2 10 L10 18" fill="none" stroke="#fff" stroke-width="2.5"/></svg></div>
  <svg class="hero-next" width="10" height="18" viewBox="0 0 10 18"><path d="M2 2 L8 9 L2 16" fill="none" stroke="#eee" stroke-width="2"/></svg>
  <div class="hero-caption">
    <h2>ST. PARTICK'S DAY MINI<br>SESSIONS $29</h2>
    <p>Includes (1) Digital file<br>Friday, March 6th<br>Saturday, March 7th</p>
    <div class="read-more">Read More</div>
  </div>
</section>

<section class="welcome abs">
  <h3>Welcome to KELVA</h3>
  <p>Kelva means to remember and for us, Kelva is the new brand name for Brightmark School Photography and Dana Holt Sports Photography.</p>
  <p>Services Offered will typically be done in volume settings.<br>Such services include:</p>
  <ul class="service-list">
    <li>School Photography</li>
    <li>Sports Photography</li>
    <li>Church Directory Photography</li>
    <li>Family Photography done for fundraising, Employee Appreciation, or Client Appreciation Purposes</li>
  </ul>
  <p class="call-line">Please call us at (555) 014-2280 ext 3<small>to schedule your event</small></p>
</section>

<div class="tile tile-studio abs" role="img" aria-label="Studio group portrait of a family in dark clothing">
  <span class="tile-icon" style="left:104px;bottom:4px">+</span>
</div>
<div class="studio-panel abs">
  <h4>Studio Portrait</h4>
  <p>At vero eos et accusamus et iusto odio un dignissimos ducimus qui voluptatum un deleniti atque sits</p>
</div>
<div class="tile tile-sports abs" role="img" aria-label="Collage of volleyball and soccer players in action">
  <span class="tile-icon" style="left:104px;bottom:4px">+</span>
</div>

<svg class="carousel-arrow abs" style="left:96px" width="16" height="26" viewBox="0 0 16 26"><path d="M13 3 L4 13 L13 23" fill="none" stroke="#444" stroke-width="4"/></svg>
<svg class="carousel-arrow abs" style="left:1088px" width="16" height="26" viewBox="0 0 16 26"><path d="M3 3 L12 13 L3 23" fill="none" stroke="#444" stroke-width="4"/></svg>

<article class="card abs" style="left:163px">
  <div class="card-photo" role="img" aria-label="Smiling family portraits" style="background:linear-gradient(135deg,#e9ddd2 0%,#d9b59a 30%,#b0603f 60%,#e8d2c0 100%)"></div>
  <h5>Fundraising</h5>
  <p>Schedule your family at one of our Fundraising Events.</p>
</article>
<article class="card abs" style="left:387px">
  <div class="card-photo" role="img" aria-label="Church directory booklets and a cross" style="background:linear-gradient(135deg,#7e1f25 0%,#d8d2cb 45%,#8aa0b8 75%,#5a6a7a 100%)"></div>
  <h5>Church Directories</h5>
  <p>Schedule your Family Portrait at your Church Directory photo shoot.</p>
</article>
<article class="card abs" style="left:611px">
  <div class="card-photo" role="img" aria-label="High school crests" style="background:linear-gradient(135deg,#f4f4f4 0%,#c9c4d8 45%,#f0e6e6 75%,#b8a0a0 100%)"></div>
  <h5>Super senior Days</h5>
  <p>Click here | Schedule your 2015 Senior Portrait photo shoot.</p>
</article>
<article class="card abs" style="left:835px">
  <div class="card-photo" role="img" aria-label="Volleyball team and sports photo collage" style="background:linear-gradient(135deg,#2c3a6a 0%,#b3283a 45%,#d8c8b8 100%)"></div>
  <h5>School Photography</h5>
  <p>Schedule your portrait at your School Photography photo shoot.</p>
</article>

<h2 class="video-heading abs">START VIDEO</h2>
<p class="video-sub abs">If your high school has contracted with Kelva Photography to provide your senior yearbook photo,<br>this video explains what options are available to you.</p>

<section class="video abs">
  <div class="video-frame" role="img" aria-label="Video still of a senior girl posing in a photo studio"></div>
  <div class="video-thumb" role="img" aria-label="Channel thumbnail portrait"></div>
  <div class="video-title">Senior Portraits by Dana Holt and Kelva Photography</div>
  <div class="video-from">from <span>Your Channel</span></div>
  <div class="video-actions">
    <div><svg width="20" height="18" viewBox="0 0 20 18"><path d="M10 17 L2 9 A4.5 4.5 0 0 1 10 3 A4.5 4.5 0 0 1 18 9 Z" fill="#fff"/></svg>LIKE</div>
    <div><svg width="20" height="18" viewBox="0 0 20 18"><path d="M3 15 L10 4 L17 15" fill="none" stroke="#fff" stroke-width="3"/></svg>SHARE</div>
    <div><svg width="22" height="16" viewBox="0 0 22 16"><path d="M7 3 L2 8 L7 13 M15 3 L20 8 L15 13" fill="none" stroke="#fff" stroke-width="2.5"/></svg>EMBED</div>
  </div>
  <div class="video-controls">
    <div class="play-btn"><svg width="20" height="22" viewBox="0 0 20 22"><path d="M2 1 L19 11 L2 21 Z" fill="#fff"/></svg></div>
    <div class="scrub">
      <span class="time-tag">00:34</span>
      <div class="track"><span class="loaded"></span><span class="played"></span></div>
      <svg width="30" height="14" viewBox="0 0 30 14"><g fill="#27a6e6"><rect x="0" y="0" width="3" height="14"/><rect x="6" y="0" width="3" height="14"/><rect x="12" y="0" width="3" height="14"/><rect x="18" y="0" width="3" height="14"/><rect x="24" y="0" width="3" height="14"/></g></svg>
      <i class="hd">HD</i>
      <svg width="16" height="16" viewBox="0 0 16 16"><path d="M1 6 V1 H6 M10 1 H15 V6 M15 10 V15 H10 M6 15 H1 V10" fill="none" stroke="#fff" stroke-width="2"/></svg>
    </div>
  </div>
</section>

<div class="footer-brand abs">
  <div class="brand"><span class="brand-name">Kelva</span><span class="brand-dot"></span></div>
  <div class="sub">Kelva Photography</div>
</div>
<div class="book-btn book-bottom abs">Click here to book your<b>KELVA EXPERIENCE</b></div>

<footer class="footer-bar abs">
  <span>© 2015 Kelva Photography. All rights reserved</span>
  <span>Legal Notice</span>
  <span>Terms &amp; Conditions</span>
  <div class="footer-social" aria-label="Social links">
    <span class="on"></span><span></span><span></span><span></span><span></span><span></span><span></span><span></span><span></span>
  </div>
</footer>

</body>
</html>
```